Website for Arts Studios including Audio, Video and Performing Arts

Creating an engaging and informative website for Brightmoor Studios is a paramount endeavor that demands careful consideration of the brand's identity, values, and goals. This project offers a unique opportunity to showcase the studio's multifaceted offerings and establish a strong online presence. In order to fulfill the objectives outlined in the website brief, we will design a comprehensive, user-friendly, and aesthetically pleasing website that not only introduces Brightmoor Studios to the world but also provides a seamless experience for visitors.

The website's primary focus is to present Brightmoor Studios as a hub for creativity, wellness, and community engagement. To achieve this, we will construct various sections that highlight the studio's features and appeal to a broad audience:

1. **Classes and Studio Sessions**: A central element of the website will be dedicated to showcasing the various classes and studio sessions offered by Brightmoor Studios. This section will provide detailed information about the classes available, their schedules, and the instructors, encouraging visitors to explore and sign up for sessions that align with their interests and needs.

2. **About Section**: This segment will provide an in-depth insight into the ethos and history of Brightmoor Studios. It will introduce the founders, their vision, and the core values that underpin the studio's operations. We will incorporate compelling storytelling and visuals to create a strong emotional connection with visitors.

3. **Staffing Section**: Highlighting the talented and dedicated team behind Brightmoor Studios is crucial. This section will include profiles of instructors, trainers, and support staff, enabling visitors to get to know the individuals who make the studio a vibrant and welcoming place.

4. **Phases Description**: To communicate the studio's growth and evolution, we will incorporate a section outlining the different phases of development. Phase 1, Phase 2, and future phases will be described, giving visitors a clear understanding of Brightmoor Studios' ongoing commitment to innovation and expansion.

5. **Contact Us**: A user-friendly contact section will be integrated to facilitate easy communication between Brightmoor Studios and its audience. Visitors can inquire about classes, studio bookings, or any other inquiries, fostering a sense of accessibility and approachability.

In addition to these core sections, the website will also prioritize responsive design and easy navigation, ensuring that users can access the information they seek on various devices and screen sizes. We will focus on creating a visually appealing and cohesive design, using a color palette and imagery that aligns with the studio's branding.

In conclusion, the website we propose for Brightmoor Studios goes beyond being a mere online presence; it serves as a dynamic platform to introduce the studio to the world. By combining compelling content, user-friendly features, and a commitment to capturing the essence of Brightmoor Studios, our design will help the studio engage with a global audience, promote its mission, and foster a sense of belonging among its visitors.

Target Market(s)

Artists in the DFW metroplec

Industry/Entity Type

Entertainment/Music/Performing Arts

Coding

Coded - Design and coding required

Number of Pages Required

1 page

Font styles to use
Other font styles liked:
• Cachet should be included within the font set.

Colors
FFC000
F8CF3A
FAE287
FDF2CF
FEFAEE

Requirements
Must have
• The sections in the description
Nice to have
• A floating video in the background of the landing page
Should not have
• any ecommerce bits

```html
<!DOCTYPE html>
<html lang="en">
<head>
<meta charset="utf-8">
<title>Brightmoor Studios</title>
<link rel="stylesheet" href="https://fonts.googleapis.com/css2?family=Roboto:wght@300;400;500;700&display=swap">
<style>
:root{
  --gold:#ffc000;
  --gold-soft:#f8cf3a;
  --butter:#fae287;
  --cream:#fdf2cf;
  --ivory:#fefaee;
  --gold-deep:#b88600;
  --ink:#1c1a14;
  --text:#2b2820;
  --night:#221c0e;
  --white:#ffffff;
}
*{box-sizing:border-box;margin:0;padding:0}
html,body{width:1200px;height:3836px;overflow:hidden}
body{position:relative;font-family:'Roboto',sans-serif;color:var(--text);background:var(--white)}
.abs{position:absolute}
.btn{position:absolute;background:var(--gold);color:var(--ink);font-size:12px;font-weight:500;display:flex;align-items:center;justify-content:center}

/* hero */
.hero{left:0;top:0;width:1200px;height:613px;background:linear-gradient(180deg,#3a2c14 0%,#6b5326 30%,#8a6b2e 45%,#4d3a18 70%,#261c0b 100%)}
.nav{left:122px;top:28px;display:flex;gap:28px;font-size:11px;color:var(--white)}
.brand-top{left:0;width:1200px;top:24px;text-align:center;color:var(--white);font-size:18px;font-weight:500}
.phone{left:864px;top:33px;font-size:11px;color:var(--white);letter-spacing:.5px}
.membership{left:962px;top:24px;width:116px;height:33px;font-size:10px;letter-spacing:.6px}
.welcome{left:0;width:1200px;top:172px;text-align:center;color:var(--white);font-size:33px;font-weight:300}
.hero-title{left:0;width:1200px;top:204px;text-align:center;color:var(--white);font-size:70px;font-weight:400;letter-spacing:1px}
.hero-copy{left:306px;width:588px;top:292px;text-align:center;color:var(--white);font-size:12.5px;line-height:22px}
.get-started{left:546px;top:371px;width:117px;height:35px}

/* classes */
.services-bg{left:0;top:613px;width:1200px;height:507px;background:var(--ivory)}
.tabs{left:112px;top:613px;width:975px;height:93px;background:var(--white);box-shadow:0 6px 18px rgba(0,0,0,.08);display:flex}
.tab{flex:1;display:flex;flex-direction:column;align-items:center;justify-content:center;gap:8px;font-size:12px;color:var(--ink);position:relative}
.tab+.tab::before{content:"";position:absolute;left:0;top:14px;bottom:14px;width:1px;background:#e6dcc0}
.tab.active{background:var(--gold);flex:0 0 201px}
.tab.active::before{display:none}
.tab svg{width:42px;height:42px}
.class-photo{left:112px;top:768px;width:479px;height:289px;background:linear-gradient(120deg,#3b2d1a 0%,#8a6428 45%,#f0d58a 100%)}
.class-title{left:645px;top:798px;font-size:37px;font-weight:400;color:var(--ink)}
.class-copy{left:648px;top:850px;width:430px;font-size:12px;line-height:21px;color:var(--ink)}
.meta{top:924px;display:flex;align-items:center;gap:8px;font-size:12px;color:var(--ink)}
.meta .dot{width:30px;height:30px;border-radius:50%;background:var(--gold);display:flex;align-items:center;justify-content:center}
.contact-btn{left:648px;top:972px;width:116px;height:39px}

/* about */
.about-bg{left:0;top:1120px;width:1200px;height:905px;background:var(--cream)}
.about-title{left:112px;top:1275px;font-size:37px;font-weight:400;color:var(--ink)}
.about-copy{left:112px;top:1345px;width:398px;font-size:12px;line-height:29.3px;color:var(--ink)}
.learn-btn{left:113px;top:1797px;width:116px;height:39px}
.stage-photo{left:677px;top:1632px;width:410px;height:307px;background:linear-gradient(160deg,#2a1e10 0%,#7a5820 40%,#1c1710 75%,#c79a35 100%)}
.singer-frame{left:541px;top:1199px;width:471px;height:556px;background:var(--white)}
.singer-photo{left:548px;top:1206px;width:457px;height:542px;background:linear-gradient(150deg,#1d1a14 0%,#5a4420 35%,#e2b84a 65%,#fae287 100%)}
.about-side{left:1022px;top:1258px;width:60px;height:313px;display:flex;align-items:center;justify-content:center}
.about-side span{transform:rotate(90deg);white-space:nowrap;font-size:66px;color:var(--gold-deep);letter-spacing:1px;font-weight:400}

/* team */
.team-photo{left:0;top:2025px;width:1200px;height:488px;background:linear-gradient(90deg,#8c8c8c 0%,#cfcfcf 35%,#a9a9a9 55%,#e3e3e3 80%,#9c9c9c 100%)}
.team-tag{left:330px;top:2055px;width:152px;height:49px;background:var(--white);color:var(--gold-deep);font-size:25px;display:flex;align-items:center;justify-content:center;letter-spacing:.5px}

/* phases */
.steps-bg{left:0;top:2513px;width:1200px;height:443px;background:var(--cream)}
.steps-title{left:0;width:1200px;top:2562px;text-align:center;font-size:37px;font-weight:400;color:var(--ink)}
.steps-svg{left:0;top:2513px;width:1200px;height:443px}
.step-label{top:2750px;width:180px;text-align:center;color:var(--ink);font-size:20px;letter-spacing:.5px}
.step-copy{top:2803px;width:160px;text-align:center;font-size:11.5px;line-height:19px;color:var(--ink)}

/* contact */
.visitor-photo{left:112px;top:3020px;width:488px;height:495px;background:linear-gradient(140deg,#fae287 0%,#fefaee 45%,#f3e3b0 100%)}
.form-frame{left:600px;top:3020px;width:487px;height:495px;background:var(--gold)}
.form-panel{left:618px;top:3038px;width:453px;height:458px;background:var(--cream)}
.form-title{left:618px;width:453px;top:3056px;text-align:center;font-size:36px;font-weight:400;color:var(--ink)}
.field{position:absolute;background:var(--white);font-size:11px;color:#5a5446;padding:0 18px;display:flex;align-items:center}
.field.msg{align-items:flex-start;padding-top:16px}
.submit{left:640px;top:3429px;width:116px;height:37px}

/* footer */
.footer{left:0;top:3578px;width:1200px;height:258px;background:var(--night)}
.f-brand{left:122px;top:3628px;font-size:18px;font-weight:500;color:var(--white)}
.f-text{font-size:11px;line-height:17px;color:var(--white)}
.f-head{font-size:14px;color:var(--white)}
.f-list{list-style:none;font-size:11px;line-height:19.5px;color:var(--white)}
.social{list-style:none;font-size:11px;color:var(--white)}
.social li{display:flex;align-items:center;gap:9px;height:25px}
.social i{width:16px;height:16px;background:var(--gold);display:block}
.subscribe{left:771px;top:3705px;display:flex}
.subscribe .email{width:176px;height:30px;background:var(--white);color:#5a5446;font-size:8px;padding-left:8px;display:flex;align-items:center}
.subscribe .go{width:68px;height:30px;background:var(--gold);color:var(--ink);font-size:12px;font-weight:500;display:flex;align-items:center;justify-content:center}
.copyright{left:0;width:1200px;top:3809px;text-align:center;font-size:10.5px;color:var(--white)}
</style>
</head>
<body>

<!-- Hero -->
<section class="abs hero" role="img" aria-label="Warm lit performance stage with a microphone stand and studio lights"></section>
<nav class="abs nav"><span>Home</span><span>Classes</span><span>Studios</span><span>Team</span><span>About Us</span></nav>
<div class="abs brand-top">Brightmoor Studios</div>
<div class="abs phone">123 - 456 - 7890</div>
<div class="btn membership">MEMBERSHIP</div>
<div class="abs welcome">Welcome to</div>
<h1 class="abs hero-title">Brightmoor Studios</h1>
<p class="abs hero-copy">A home for audio, video and performing arts in the DFW metroplex. Record your next track, shoot your next film or take the stage in classes and studio sessions led by working artists who love to share their craft.</p>
<div class="btn get-started">Get started</div>

<!-- Classes and studio sessions -->
<div class="abs services-bg"></div>
<div class="abs tabs">
  <div class="tab active">
    <svg viewBox="0 0 42 42" fill="none" stroke="#1c1a14" stroke-width="1.6"><rect x="15" y="4" width="12" height="20" rx="6"/><path d="M10 18c0 6 5 11 11 11s11-5 11-11M21 29v7M14 36h14"/></svg>
    Recording Studio
  </div>
  <div class="tab">
    <svg viewBox="0 0 42 42" fill="none" stroke="#b88600" stroke-width="1.6"><rect x="4" y="12" width="24" height="18" rx="2"/><path d="M28 18l10-6v18l-10-6z"/></svg>
    Video Production
  </div>
  <div class="tab">
    <svg viewBox="0 0 42 42" fill="none" stroke="#b88600" stroke-width="1.6"><rect x="5" y="8" width="32" height="28" rx="2"/><path d="M5 15h32M13 4v7M29 4v7"/><path d="M10 21h4M19 21h4M28 21h4M10 27h4M19 27h4M28 27h4M10 32h4M19 32h4"/></svg>
    Daily Classes &amp; Programs
  </div>
  <div class="tab">
    <svg viewBox="0 0 42 42" fill="none" stroke="#b88600" stroke-width="1.6"><path d="M6 34h30M9 34V14h24v20"/><path d="M9 14c4 4 8 4 12 0c4 4 8 4 12 0"/><path d="M21 8v6"/></svg>
    Performing Arts Stage
  </div>
  <div class="tab">
    <svg viewBox="0 0 42 42" fill="none" stroke="#b88600" stroke-width="1.6"><path d="M16 30V8l18-4v22"/><circle cx="12" cy="30" r="4"/><circle cx="30" cy="26" r="4"/></svg>
    Music Lessons
  </div>
</div>
<div class="abs class-photo" role="img" aria-label="Artist singing into a microphone in a recording booth"></div>
<h2 class="abs class-title">Recording Studio</h2>
<p class="abs class-copy">Book tracking, mixing and podcast sessions in our 11,000 square foot studio space. Working engineers and carefully tuned rooms make for a sound you will love.</p>
<div class="abs meta" style="left:651px">
  <span class="dot"><svg width="18" height="18" viewBox="0 0 18 18" fill="none" stroke="#1c1a14" stroke-width="1.4"><circle cx="9" cy="9" r="7"/><path d="M9 5v4l3 2"/></svg></span>
  Time : 4:00pm - 7:00pm
</div>
<div class="abs meta" style="left:832px">
  <span class="dot"><svg width="18" height="18" viewBox="0 0 18 18" fill="none" stroke="#1c1a14" stroke-width="1.4"><rect x="2" y="3" width="14" height="13" rx="1"/><path d="M2 7h14M6 1v3M12 1v3"/></svg></span>
  Day : Mondays - Wednesdays
</div>
<div class="btn contact-btn">Contact Us</div>

<!-- About -->
<div class="abs about-bg"></div>
<h2 class="abs about-title">About Us</h2>
<p class="abs about-copy">Brightmoor Studios began as a small rehearsal room shared by a handful of local musicians, filmmakers and dancers who wanted a place to create together. Our founders believed that every artist deserves good gear, honest feedback and a stage to stand on. Today the studio brings recording suites, a video production floor and a performance hall under one roof. We value curiosity, craft and community, and we keep our doors open to beginners and seasoned pros alike. Every class, session and showcase is built around one idea: art grows best when people make it side by side. From first demos to opening nights, we are proud to help artists across the metroplex find their voice, sharpen their skills and share their work with the world around them.</p>
<div class="btn learn-btn">Learn More</div>
<div class="abs stage-photo" role="img" aria-label="Mixing console with glowing faders in a dim control room"></div>
<div class="abs singer-frame"></div>
<div class="abs singer-photo" role="img" aria-label="Dancer performing on stage under warm spotlights"></div>
<div class="abs about-side"><span>ABOUT US</span></div>

<!-- Team -->
<section class="abs team-photo" role="img" aria-label="Black and white group photo of the studio instructors and staff with one highlighted in colour"></section>
<div class="abs team-tag">MENTOR</div>

<!-- Phases -->
<div class="abs steps-bg"></div>
<h2 class="abs steps-title">Our Phases</h2>
<svg class="abs steps-svg" viewBox="0 0 1200 443" fill="none">
  <g stroke="#1c1a14" stroke-width="2.4">
    <path d="M413 168 A126 126 0 1 0 440 290"/>
    <path d="M687 168 A126 126 0 1 0 714 290"/>
    <path d="M737 228 A127 127 0 1 1 770 338"/>
  </g>
  <g fill="#fff" stroke="#1c1a14" stroke-width="2">
    <circle cx="413" cy="168" r="4"/>
    <circle cx="687" cy="168" r="4"/>
    <circle cx="770" cy="338" r="4"/>
  </g>
  <rect x="170" y="234" width="851" height="36" fill="#ffc000"/>
  <g stroke="#1c1a14" stroke-width="2.4" stroke-linecap="round" stroke-linejoin="round">
    <path d="M440 290 L452 262 L490 262 M478 254 L492 262 L478 270"/>
    <path d="M714 290 L726 262 L758 262 M746 254 L760 262 L746 270"/>
  </g>
  <g stroke="#b88600" stroke-width="1.8" stroke-linecap="round" stroke-linejoin="round">
    <rect x="314" y="176" width="12" height="20" rx="6"/><path d="M308 190c0 7 5 11 12 11s12-4 12-11M320 201v8M313 209h14"/>
    <rect x="578" y="184" width="22" height="16" rx="2"/><path d="M600 189l10-5v16l-10-5z"/>
    <path d="M845 212h32M848 212v-18h26v18M848 194c4 4 9 4 13 0c4 4 9 4 13 0"/>
  </g>
</svg>
<div class="abs step-label" style="left:230px">PHASE 1</div>
<div class="abs step-label" style="left:507px">PHASE 2</div>
<div class="abs step-label" style="left:773px">PHASE 3</div>
<p class="abs step-copy" style="left:240px">Open recording suites and weekly classes for local artists.</p>
<p class="abs step-copy" style="left:517px">Add a video floor and a performance hall for live shows.</p>
<p class="abs step-copy" style="left:783px">Grow residencies, tours and partnerships across the region.</p>

<!-- Contact -->
<div class="abs visitor-photo" role="img" aria-label="Smiling musician holding a guitar in the studio lounge"></div>
<div class="abs form-frame"></div>
<div class="abs form-panel"></div>
<h2 class="abs form-title">Get in Touch</h2>
<div class="field" style="left:639px;top:3124px;width:197px;height:43px">Name :</div>
<div class="field" style="left:850px;top:3124px;width:198px;height:43px">Email :</div>
<div class="field" style="left:639px;top:3186px;width:197px;height:44px">Interested :</div>
<div class="field" style="left:850px;top:3186px;width:198px;height:44px">Session type :</div>
<div class="field" style="left:639px;top:3250px;width:197px;height:44px">Subject :</div>
<div class="field" style="left:850px;top:3250px;width:198px;height:44px">Phone :</div>
<div class="field msg" style="left:639px;top:3313px;width:409px;height:94px">message :</div>
<div class="btn submit">Submit</div>

<!-- Footer -->
<footer class="abs footer"></footer>
<div class="abs f-brand">Brightmoor Studios</div>
<p class="abs f-text" style="left:122px;top:3657px;width:150px">Audio, video and performing arts studios for the DFW metroplex.</p>
<div class="abs f-head" style="left:365px;top:3633px">Menu</div>
<ul class="abs f-list" style="left:365px;top:3652px"><li>Home</li><li>Classes</li><li>Studios</li><li>Team</li><li>About Us</li></ul>
<div class="abs f-head" style="left:564px;top:3633px">Follow Us</div>
<ul class="abs social" style="left:566px;top:3655px">
  <li><i></i>Circlepage</li><li><i></i>Chirpline</li><li><i></i>Snapframe</li><li><i></i>Vidstream</li>
</ul>
<div class="abs f-head" style="left:771px;top:3633px">Stay Connected</div>
<p class="abs f-text" style="left:771px;top:3653px;width:190px">Sign up with your email address to receive news &amp; updates.</p>
<div class="abs subscribe"><div class="email">Email Address</div><div class="go">Sign up</div></div>
<div class="abs copyright">Copyright © 2010-2023 Brightmoor Studios. All rights reserved.</div>

</body>
</html>
```